Cognitive therapist.

I am a therapist and my main work is with clients who have depression and anxiety disorders.

I need something reasonably plain. Cognitive therapy is a very pragmatic approach to dealing with problems, so it isn't new agey (no offence to new age therapies at all)

Hi everyone, I am currently looking at a particular design that I will most likely go with. Cheers, Mel

Mel Tarrow
Cognitive Therapist
BA, PG Dip Mental Health,
PG Dip Cog Beh Therapy
MKLPT

The Larchmont Rooms,
Level One
57 Quillon Parade
Cnr Fenwick St & Quillon Parade
P O Box 38 215
WELLINGTON 6281

Phone: 027 534 2870 Email: mtarrow@vexmail.co.nz

www.meltarrow.co.nz

• No illustration, or colour. not old style fonts.

```html
<!DOCTYPE html>
<html lang="en">
<head>
<meta charset="utf-8">
<title>Mel Tarrow – Cognitive Therapist</title>
<link rel="stylesheet" href="https://fonts.googleapis.com/css2?family=Cinzel:wght@400&family=EB+Garamond:wght@400&family=PT+Sans:wght@400&display=swap">
<style>
  :root {
    --backdrop: #2b2b2b;
    --card: #e9e9e9;
    --card-edge: #d4d4d4;
    --ink: #2f2f2f;
    --band: #3a3a3a;
    --band-text: #f1f1f1;
    --ornament: #b9b9b9;
  }
  * { margin: 0; padding: 0; box-sizing: border-box; }
  html, body {
    width: 1200px; height: 717px; overflow: hidden;
    background: var(--backdrop);
  }
  .card {
    position: absolute; left: 150px; top: 98px;
    width: 900px; height: 520px;
    background: linear-gradient(160deg, #f2f2f2, var(--card) 55%, var(--card-edge));
    color: var(--ink);
  }
  .card-frame { position: absolute; inset: 0; }
  .ornament-top {
    position: absolute; left: 370px; top: 40px; width: 160px; height: 52px;
    background: var(--ornament); border-radius: 26px;
  }
  .ornament-small {
    position: absolute; left: 430px; top: 396px; width: 40px; height: 14px;
    background: var(--ornament); border-radius: 7px;
  }
  .centered { position: absolute; left: 0; width: 100%; text-align: center; }
  .name {
    top: 118px; font-family: "Cinzel", serif; font-size: 54px;
    letter-spacing: 2px; line-height: 1;
  }
  .credentials {
    top: 182px; font-family: "PT Sans", sans-serif; font-size: 19px; line-height: 1.25;
  }
  .phone-band { position: absolute; left: 110px; top: 240px; width: 680px; height: 68px; }
  .phone {
    top: 250px; font-family: "EB Garamond", serif; font-size: 40px;
    color: var(--band-text); letter-spacing: 3px; line-height: 48px;
  }
  .address {
    top: 330px; font-family: "PT Sans", sans-serif; font-size: 18px;
    text-transform: uppercase; letter-spacing: 0.5px; line-height: 1.4;
  }
  .web {
    top: 438px; font-family: "EB Garamond", serif; font-size: 25px; letter-spacing: 1px;
  }
</style>
</head>
<body>
  <div class="card">
    <svg class="card-frame" width="900" height="520" viewBox="0 0 900 520" aria-hidden="true">
      <g fill="none" stroke="var(--ink)" stroke-width="1.5">
        <rect x="22" y="22" width="856" height="476"/>
        <rect x="30" y="30" width="840" height="460" stroke-width="1"/>
        <line x1="90" y1="102" x2="810" y2="102"/>
        <line x1="150" y1="424" x2="750" y2="424" stroke-width="1"/>
      </g>
      <g fill="var(--ink)">
        <rect x="15" y="15" width="16" height="16"/>
        <rect x="869" y="15" width="16" height="16"/>
        <rect x="15" y="489" width="16" height="16"/>
        <rect x="869" y="489" width="16" height="16"/>
        <path d="M84 102 l6 -5 l6 5 l-6 5z"/>
        <path d="M804 102 l6 -5 l6 5 l-6 5z"/>
      </g>
      <path class="band-shape" fill="var(--band)"
        d="M124 240 H776 v10 h14 v48 h-14 v10 H124 v-10 h-14 v-48 h14z" transform="translate(0,0)"/>
    </svg>

    <div class="ornament-top" role="img" aria-label="Decorative scroll flourish"></div>

    <div class="centered name">MEL TARROW</div>
    <div class="centered credentials">
      Cognitive Therapist BA-PG Dip Mental Health-<br>
      PG Dip Cog Beh Therapy MKLPT The Larchmont Rooms
    </div>

    <div class="centered phone">027 - 534 - 2870</div>

    <div class="centered address">
      Level One 57 Quillon Parade Cnr Fenwick St &amp; Quillon Parade<br>
      P O Box 38 215 Wellington 6281
    </div>

    <div class="ornament-small" role="img" aria-label="Small decorative knot"></div>

    <div class="centered web">mtarrow@vexmail.co.nz &nbsp;-&nbsp; www.meltarrow.co.nz</div>
  </div>
</body>
</html>
```